Copper Ridge Garage Door Sales & Repair needs a Business Card Design

I need a business card design to go with our new business logo that was created a few months ago.

Copper Ridge Garage Door specializes in selling and installing new garage doors, and new garage door openers. We also take care of all repairs to existing garage doors and garage door openers. All makes and models.

Target Market(s)

Home-owners, renters, anyone who lives in a house and has a garage. Residential and commercial garages.

Industry/Entity Type

Home Improvement

Contact Information for Business Card

I would like the business cards to have rounded corners and be double-sided. My old logo is still on my website at www.copperridgegarage.example. If I was going to incorporate a secondary color on the business cards, I think that orange is a good choice (especially since blue and orange are the colors of our Tulsa Kestrels), but I'm not opposed to seeing a different color if another color works better with my logo colors. I have two logo colors. One designed for a white background and one designed for a darker background. I'm not opposed to using both. Maybe a dark background with the white logo on one side, and a white background with the other logo color on the other side.

My business is a small, locally owned business that I am trying to grow. But I would like my business cards to look very professional. Like we have been in business for a long time. I like traditional to modern looking cards. Just something bold and memorable. My full company name is Copper Ridge Garage Door Sales & Repair. But you can just do COPPER RIDGE GARAGE DOOR, if that works better.

Font styles to use
Serif
Script

Requirements
Must have
• Rounded corners
• Double-sided
• 3-D Elements. Layering of some sort (a sketch of a garage door or a 3rd color (orange) brought in some how. I really like watermarks.
• Matte cards that you can write on.
• White on one side. (Or the lighter blue in my logo). Darker blue logo color on the other side.
• I would like our tag line on the cards somewhere... "For All Your Garage Door Needs".
• I would also like "Call For a FREE Estimate" by the phone number.
• And "Serving the Greater Metro Denver Area" somewhere on the card as well.
Nice to have
• Refer to "Business Card Details" above.

```html
<!DOCTYPE html>
<html lang="en">
<head>
<meta charset="utf-8">
<title>Copper Ridge Garage Door – Business Card</title>
<link rel="stylesheet" href="https://fonts.googleapis.com/css2?family=Open+Sans:wght@400;600;700&family=Roboto+Slab:wght@400;700&display=swap">
<style>
  :root {
    --backdrop: #3a322d;
    --card-dark: #0d0d0e;
    --card-light: #f4f5f8;
    --brand-blue: #6d7ca3;
    --brand-navy: #2f3c5e;
    --accent-orange: #e07a2c;
    --ink-light: #e4e6ec;
    --ink-soft: #b9bdc8;
    --ink-dark: #2a2d36;
    --rule: #3a3b40;
  }
  * { box-sizing: border-box; margin: 0; padding: 0; }
  html, body {
    width: 1200px; height: 844px; overflow: hidden;
    background: var(--backdrop);
    font-family: "Open Sans", Arial, sans-serif;
  }
  .stage { position: relative; width: 1200px; height: 844px; }
  .card {
    position: absolute; top: 272px;
    width: 525px; height: 300px;
    border-radius: 16px;
    box-shadow: 0 14px 34px rgba(0,0,0,.45);
    overflow: hidden;
  }
  .card-front { left: 50px; background: var(--card-dark); color: var(--ink-light); }
  .card-back { left: 625px; background: var(--card-light); color: var(--ink-dark); }

  .accent-bar {
    position: absolute; left: 0; right: 0; bottom: 0;
    height: 6px; background: var(--accent-orange);
  }

  /* front */
  .brand-name {
    position: absolute; top: 30px; left: 0; right: 0;
    text-align: center; color: var(--brand-blue);
    font-family: "Roboto Slab", Georgia, serif;
    font-weight: 700; font-size: 30px; letter-spacing: 1px;
    text-transform: uppercase; line-height: 1.12;
  }
  .service-area {
    position: absolute; top: 114px; left: 0; right: 0;
    text-align: center; font-weight: 600; font-size: 15px; color: var(--ink-light);
  }
  .contact-split {
    position: absolute; top: 154px; left: 0; right: 0;
    display: flex; justify-content: center;
  }
  .person { text-align: right; padding-right: 20px; border-right: 1px solid var(--accent-orange); }
  .person-name {
    font-family: "Roboto Slab", Georgia, serif;
    font-size: 20px; color: var(--ink-light); line-height: 1.25;
  }
  .person-title { font-size: 13px; color: var(--ink-soft); margin-bottom: 14px; }
  .person-address { font-size: 14px; line-height: 1.3; color: var(--ink-light); }
  .contact-list { list-style: none; padding-left: 20px; padding-top: 4px; }
  .contact-list li {
    display: flex; align-items: center; gap: 10px;
    font-size: 13.5px; line-height: 1.75; color: var(--ink-light);
  }
  .contact-list svg { width: 12px; height: 12px; fill: var(--accent-orange); flex: none; }

  /* back */
  .estimate {
    position: absolute; top: 30px; left: 0; right: 0;
    text-align: center; font-size: 13px; line-height: 1.3; color: var(--ink-dark);
  }
  .estimate strong { font-weight: 700; font-size: 15px; color: var(--accent-orange); }
  .estimate-phone { font-size: 14px; font-weight: 600; }
  .back-brand {
    position: absolute; top: 98px; left: 0; right: 0;
    display: flex; align-items: center; justify-content: center; gap: 14px;
  }
  .back-brand-dot {
    width: 54px; height: 54px; border-radius: 50%;
    border: 3px solid var(--brand-navy); flex: none;
  }
  .back-brand-name {
    color: var(--brand-navy);
    font-family: "Roboto Slab", Georgia, serif;
    font-weight: 700; font-size: 26px;
    text-transform: uppercase; line-height: 1.15; letter-spacing: 1px;
  }
  .tagline {
    position: absolute; top: 232px; left: 0; right: 0;
    text-align: center; font-weight: 600; font-size: 15px; color: var(--brand-navy);
  }
</style>
</head>
<body>
<main class="stage">

  <section class="card card-front" aria-label="Business card front">
    <h1 class="brand-name">Copper Ridge<br>Garage Door</h1>
    <p class="service-area">Serving the Greater Metro Denver Area</p>
    <div class="contact-split">
      <div class="person">
        <p class="person-name">Daniel Hartley</p>
        <p class="person-title">Managing Director</p>
        <p class="person-address">4810 Ridgeline Avenue<br>Tulsa, OK 74103</p>
      </div>
      <ul class="contact-list">
        <li><svg viewBox="0 0 24 24"><path d="M6.6 10.8a15.1 15.1 0 0 0 6.6 6.6l2.2-2.2a1 1 0 0 1 1-.25 11.4 11.4 0 0 0 3.6.57 1 1 0 0 1 1 1V20a1 1 0 0 1-1 1A17 17 0 0 1 3 4a1 1 0 0 1 1-1h3.5a1 1 0 0 1 1 1c0 1.25.2 2.45.57 3.57a1 1 0 0 1-.25 1z"/></svg>(555)-014-2290</li>
        <li><svg viewBox="0 0 24 24"><path d="M6 2h10v6H6zM4 9h16a2 2 0 0 1 2 2v9H2v-9a2 2 0 0 1 2-2zm3 4v2h3v-2zm5 0v2h3v-2zm-5 4v2h3v-2zm5 0v2h3v-2z"/></svg>555-014-7781</li>
        <li><svg viewBox="0 0 24 24"><path d="M2 5h20v14H2zm2 2v.5l8 5 8-5V7l-8 5z"/></svg>info@copperridgegarage.example</li>
        <li><svg viewBox="0 0 24 24"><circle cx="12" cy="12" r="10"/></svg>www.copperridgegarage.example</li>
      </ul>
    </div>
    <span class="accent-bar" aria-hidden="true"></span>
  </section>

  <section class="card card-back" aria-label="Business card back">
    <p class="estimate">Call For a <strong>FREE</strong> Estimate<br><span class="estimate-phone">555 014 2290</span></p>
    <div class="back-brand">
      <span class="back-brand-dot" aria-hidden="true"></span>
      <p class="back-brand-name">Copper Ridge<br>Garage Door</p>
    </div>
    <p class="tagline">For All Your Garage Door Needs</p>
    <span class="accent-bar" aria-hidden="true"></span>
  </section>

</main>
</body>
</html>
```